Redesign Event Flyer for Speaker

We are re-designing our professional event flyer template with new headshot and cleaner, up-to-date design. All design details are in PDF file attached. Thank you for participating :)

Font styles to use
Sans Serif

Colors
3276b5
0355a3

Requirements
Must have
• All elements in PDF file.
Nice to have
Should not have
• Tacky or childish elements.

```html
<!DOCTYPE html>
<html lang="en">
<head>
<meta charset="utf-8">
<title>The Greatest Sale – Event Flyer</title>
<link rel="stylesheet" href="https://fonts.googleapis.com/css2?family=Oswald:wght@500;600&family=Montserrat:wght@600;700&display=swap">
<style>
  :root {
    --charcoal: #1b1d21;
    --charcoal-deep: #111214;
    --brand-blue: #3276b5;
    --brand-blue-deep: #0355a3;
    --blue-glow: #1d4f86;
    --blue-light: #4a8fd0;
    --white: #ffffff;
    --suit-navy: #23324f;
    --suit-shadow: #151c2c;
    --skin-tone: #6b4a3a;
  }
  * { margin: 0; padding: 0; box-sizing: border-box; }
  html, body {
    width: 1200px;
    height: 800px;
    overflow: hidden;
    background: var(--charcoal-deep);
  }
  .flyer {
    position: relative;
    width: 1200px;
    height: 800px;
    overflow: hidden;
    background:
      radial-gradient(ellipse 430px 540px at 600px 170px, var(--brand-blue-deep) 0%, var(--blue-glow) 40%, rgba(3,85,163,0) 100%),
      linear-gradient(90deg, var(--charcoal) 0%, #182230 45%, #182230 55%, var(--charcoal) 100%);
    font-family: "Montserrat", sans-serif;
    color: var(--white);
  }
  .speaker-portrait {
    position: absolute;
    left: 360px;
    top: 62px;
    width: 590px;
    height: 738px;
    border-radius: 250px 250px 0 0;
    background:
      radial-gradient(ellipse 115px 145px at 295px 170px, var(--skin-tone) 0%, rgba(107,74,58,0.6) 60%, rgba(107,74,58,0) 100%),
      linear-gradient(180deg, rgba(35,50,79,0) 0%, rgba(35,50,79,0.55) 38%, var(--suit-navy) 55%, var(--suit-shadow) 100%);
  }
  .brand-name {
    position: absolute;
    left: 210px;
    top: 36px;
    display: flex;
    align-items: center;
    gap: 12px;
    font-weight: 700;
    font-size: 38px;
    color: var(--blue-light);
  }
  .brand-name .brand-dot {
    width: 26px;
    height: 26px;
    border-radius: 50%;
    background: var(--blue-light);
  }
  .event-date {
    position: absolute;
    left: 818px;
    top: 22px;
    font-family: "Oswald", sans-serif;
    font-weight: 600;
    font-size: 50px;
    line-height: 1.05;
    text-transform: uppercase;
    color: var(--white);
  }
  .speaker-name {
    position: absolute;
    left: 258px;
    top: 226px;
    font-family: "Montserrat", sans-serif;
    font-weight: 700;
    font-size: 19px;
    letter-spacing: 0.5px;
    text-transform: uppercase;
    color: var(--white);
  }
  .event-title {
    position: absolute;
    left: 258px;
    top: 260px;
    font-family: "Oswald", sans-serif;
    font-weight: 600;
    font-size: 62px;
    line-height: 1.02;
    text-transform: uppercase;
    color: var(--white);
    -webkit-text-stroke: 1.5px var(--brand-blue);
  }
  .venue {
    position: absolute;
    left: 210px;
    top: 565px;
  }
  .venue-name {
    display: flex;
    align-items: center;
    gap: 12px;
    font-weight: 700;
    font-size: 40px;
    line-height: 1;
    color: var(--white);
  }
  .venue-name .venue-mark {
    width: 44px;
    height: 44px;
    background: var(--white);
  }
  .venue-subtitle {
    margin-top: 6px;
    font-weight: 700;
    font-size: 14px;
    letter-spacing: 1px;
    text-transform: uppercase;
    color: var(--white);
  }
  .venue-address {
    margin-top: 14px;
    font-weight: 700;
    font-size: 24px;
    line-height: 1.2;
    color: var(--blue-light);
  }
  .web-links {
    position: absolute;
    left: 210px;
    top: 738px;
    font-weight: 700;
    font-size: 21px;
    color: var(--white);
  }
</style>
</head>
<body>
  <main class="flyer">
    <div class="speaker-portrait" role="img" aria-label="Headshot of the speaker in a navy suit and white open-collar shirt, smiling"></div>

    <div class="brand-name"><span class="brand-dot"></span>Signwright</div>

    <p class="event-date">Friday<br>August<br>9th,2019</p>

    <p class="speaker-name">Marcus Daniel Ellery</p>
    <h1 class="event-title">The Greatest<br>Sale</h1>

    <section class="venue">
      <div class="venue-name"><span class="venue-mark"></span>FRGC</div>
      <p class="venue-subtitle">Falcon Ridge Golf Club</p>
      <p class="venue-address">4200 Lakeshore Pkwy,<br>Port Halden, Canada</p>
    </section>

    <p class="web-links">marcusellery.com | signwright.ca</p>
  </main>
</body>
</html>
```